HARLOWE CONSERVATORY SAXOPHONE SENIOR RECITAL

I need a poster design for my senior saxophone recital. The title of it is "Quill: a Voyage beneath the Edge of Tone". My concept is completely contrasting to the idea of a typical university recital. I'm so put off by the idea of "clap..clap..{play some music}..clap..clap..repeat". My recital is all based off of sound. The music I selected is all very modern (i.e Brem Ostrakel 'Warm from the First Pour' for Saxophone and Coffee Machine). I've included the Chatterbox link so you can see the picture I have in the background. I like the idea of minimal black and white photography. Also, I would like the time / date / location / etc. all included on it. Let your imaginations run wild! It's art for an artist!
https://www.chatterbox-example.net/events/412093857716230/
Target Market(s)
University Students around the Harlowe Conservatory and locals around the art district of South Beach, FL.
Industry/Entity Type
University
Look and feel

```html
<!DOCTYPE html>
<html lang="en">
<head>
<meta charset="utf-8">
<title>Quill: a Voyage beneath the Edge of Tone</title>
<link rel="stylesheet" href="https://fonts.googleapis.com/css2?family=Poppins:wght@300;400;600&display=swap">
<style>
  :root {
    --ink: #000000;
    --paper: #ffffff;
    --wall-bright: #d6d6d6;
    --wall-light: #a8a8a8;
    --wall-mid: #5e5e5e;
    --wall-dark: #1c1c1c;
    --figure-tone: #8a8a8a;
    --band: rgba(0, 0, 0, 0.78);
    --echo-soft: #333333;
    --echo-mid: #4a4a4a;
    --echo-deep: #2a2a2a;
  }
  html, body {
    margin: 0;
    padding: 0;
    overflow: hidden;
    background: var(--ink);
  }
  .poster {
    position: relative;
    width: 846px;
    height: 1200px;
    overflow: hidden;
    background: var(--ink);
    font-family: "Poppins", "Century Gothic", sans-serif;
    color: var(--paper);
  }
  .backdrop-photo {
    position: absolute;
    left: 0;
    top: 0;
    width: 846px;
    height: 1200px;
    background:
      radial-gradient(ellipse 150px 360px at 470px 540px, var(--figure-tone), rgba(138,138,138,0.35) 55%, rgba(0,0,0,0) 100%),
      radial-gradient(ellipse 300px 330px at 170px 390px, var(--wall-bright), var(--wall-light) 45%, rgba(94,94,94,0.5) 80%, rgba(0,0,0,0) 100%),
      radial-gradient(ellipse 260px 360px at 700px 420px, rgba(70,70,70,0.7), rgba(0,0,0,0) 100%),
      linear-gradient(180deg, var(--ink) 0%, var(--wall-dark) 10%, var(--wall-mid) 30%, var(--wall-dark) 60%, var(--ink) 72%, var(--ink) 100%);
  }
  .title-band {
    position: absolute;
    left: 0;
    top: 54px;
    width: 846px;
    height: 64px;
    background: var(--band);
    display: flex;
    align-items: center;
  }
  .title-band h1 {
    margin: 0 0 0 33px;
    font-size: 37px;
    font-weight: 300;
    line-height: 1;
    white-space: nowrap;
  }
  .title-band strong {
    font-weight: 600;
  }
  .event-line {
    position: absolute;
    left: 40px;
    margin: 0;
    line-height: 1;
    white-space: nowrap;
  }
  .venue {
    top: 252px;
    font-size: 29px;
    font-weight: 600;
  }
  .date {
    top: 291px;
    font-size: 45px;
    font-weight: 600;
    letter-spacing: -0.5px;
  }
  .time {
    top: 343px;
    font-size: 45px;
    font-weight: 300;
  }
  .performer {
    position: absolute;
    margin: 0;
    font-weight: 300;
    line-height: 1;
    white-space: nowrap;
  }
  .performer-echo-small {
    left: 264px;
    top: 930px;
    font-size: 32px;
    color: var(--echo-soft);
  }
  .performer-echo-large {
    left: 147px;
    top: 1040px;
    font-size: 55px;
    color: var(--echo-deep);
  }
  .performer-echo-right {
    left: 402px;
    top: 1016px;
    font-size: 40px;
    color: var(--echo-mid);
  }
  .performer-main {
    left: 222px;
    top: 950px;
    font-size: 72px;
    color: var(--paper);
  }
</style>
</head>
<body>
  <main class="poster">
    <div class="backdrop-photo" role="img" aria-label="Black and white photograph of a saxophonist in a hat and striped shirt standing in shadow against a lit, rough stone wall"></div>

    <header class="title-band">
      <h1><strong>Quill:</strong> a Voyage beneath the Edge of Tone</h1>
    </header>

    <section class="event-details">
      <p class="event-line venue">Edwin R. Morrow Recital Hall</p>
      <p class="event-line date">8 DECEMBER</p>
      <p class="event-line time">2:00 PM</p>
    </section>

    <p class="performer performer-echo-small" aria-hidden="true">Dario Menzelli</p>
    <p class="performer performer-echo-large" aria-hidden="true">Dario Menzelli</p>
    <p class="performer performer-echo-right" aria-hidden="true">Dario Menzelli</p>
    <p class="performer performer-main">Dario Menzelli</p>
  </main>
</body>
</html>
```